Stationary design for construction company

Want professional stationary and in the future brochures to use for contacting potential customers and existing customers. We are open to suggestions with existing logo. We are a contractor in the construction field that specializes in foundation plastering. We currently do other work but are looking to market and become the only go-to subcontractor for this specialty. I like the red and black contrast and the font which is "biner d". We want to present ourselves as a professional company so potential customers take us seriously.
Dunmore Stucco
86 N. Maple #415
Orem, Utah 84093
801.574.2281 Office
801.846.5037 Mobile
marla@dunmorestucco-example.com
neil@dunmorestucco-example.com
We will need to be able to edit the finished work incase future numbers, addresses and such change.
Thx
Marla
Target Market(s)
New and exiting customers in the building industry
Industry/Entity Type
Construction Company
Font styles to use
Other font styles liked:
- Biner D
Look and feel
Each slider illustrates characteristics of the customer's brand and the style your logo design should communicate.

```html
<!DOCTYPE html>
<html lang="en">
<head>
<meta charset="utf-8">
<title>Dunmore Stucco Stationery</title>
<link href="https://fonts.googleapis.com/css2?family=Lato:wght@400;700;900&display=swap" rel="stylesheet">
<style>
:root{
  --red:#c90000;
  --black:#111111;
  --ink:#444444;
  --muted:#666666;
  --paper:#ffffff;
  --paper-back:#f2f2f2;
  --rule:#e08a8a;
  --bg-top:#5e5e5e;
  --bg-mid:#6c6c6c;
  --bg-bottom:#2c2c2c;
}
*{margin:0;padding:0;box-sizing:border-box}
html,body{width:1039px;height:1200px;overflow:hidden}
body{
  position:relative;
  font-family:"Lato",Arial,sans-serif;
  background:linear-gradient(180deg,var(--bg-top) 0%,var(--bg-mid) 45%,var(--bg-bottom) 100%);
}
.sheet{position:absolute;background:var(--paper);overflow:hidden}

/* brand lockup */
.brand{position:absolute;display:flex;align-items:center}
.brand__square{background:var(--red);flex:none}
.brand__name{
  font-weight:900;color:var(--black);text-transform:uppercase;
  line-height:1.02;letter-spacing:.02em;
}

/* letterhead back */
.letterhead-back{left:94px;top:121px;width:392px;height:587px;background:var(--paper-back);border:1px solid #d8d8d8}
.letterhead-back__spine{position:absolute;left:20px;top:0;width:5px;height:100%;background:#8a8a8a}
.letterhead-back__rule{position:absolute;left:0;right:0;top:547px;height:1px;background:var(--rule)}

/* letterhead front */
.letterhead{left:542px;top:121px;width:392px;height:588px;border:1px solid #cfcfcf}
.letterhead__corner-top{position:absolute;left:0;top:0}
.letterhead__corner-bottom{position:absolute;right:0;bottom:0}
.letterhead__rule{position:absolute;left:0;right:0;height:1px;background:var(--rule)}
.recipient{position:absolute;left:32px;top:100px;font-size:8px;color:var(--ink);line-height:13.6px}
.recipient strong{font-weight:700}
.salutation{position:absolute;left:32px;top:190px;font-size:9.5px;font-weight:700;color:#333}
.letter-body{position:absolute;left:30px;width:334px;font-size:5.6px;line-height:15px;color:var(--muted);text-align:justify}
.signoff{position:absolute;font-size:8px;color:var(--ink);line-height:15px}
.letter-contact{position:absolute;left:0;right:0;font-size:5.6px;color:#222;display:flex;justify-content:center;gap:6px;align-items:center}
.letter-contact span{display:inline-flex;align-items:center;gap:3px}
.icon{width:6px;height:6px;fill:var(--red);flex:none}

/* business card */
.card{left:50px;top:779px;width:454px;height:227px}
.card__rule{position:absolute;left:0;right:0;top:189px;height:2px;background:var(--red)}
.card__emails{position:absolute;right:222px;top:198px;font-size:6.5px;line-height:10px;color:#333;text-align:right}
.card__emails div,.card__phones div{display:flex;align-items:center;gap:4px;justify-content:flex-end}
.card__phones{position:absolute;left:258px;top:198px;font-size:6.5px;line-height:10px;color:#333}
.card__phones div{justify-content:flex-start;gap:0}
.card__phones b{font-weight:400;color:var(--red)}

/* envelope */
.envelope{left:529px;top:776px;width:463px;height:231px}
.envelope__flap{position:absolute;left:0;top:0}
</style>
</head>
<body>

<!-- letterhead back -->
<section class="sheet letterhead-back">
  <div class="letterhead-back__spine"></div>
  <div class="brand" style="left:116px;top:12px;gap:7px">
    <div class="brand__square" style="width:42px;height:64px"></div>
    <div class="brand__name" style="font-size:27px">Dunmore<br>Stucco</div>
  </div>
  <div class="letterhead-back__rule"></div>
</section>

<!-- letterhead front -->
<section class="sheet letterhead">
  <svg class="letterhead__corner-top" width="50" height="57" viewBox="0 0 50 57"><polygon points="0,0 50,0 0,57" fill="var(--red)"/></svg>
  <div class="brand" style="left:56px;top:7px;gap:5px">
    <div class="brand__square" style="width:30px;height:45px"></div>
    <div class="brand__name" style="font-size:19px">Dunmore<br>Stucco</div>
  </div>
  <div class="letterhead__rule" style="top:60px"></div>

  <div class="recipient">
    <strong>Jonah Whitfield</strong><br>Owner<br>Company Name<br>Address Line1, Address Line2<br>Country -123456
  </div>
  <div class="salutation">Dear Jonah Whitfield</div>

  <p class="letter-body" style="top:210px">Lorem ipsum dolor sit amet, consectetur adipiscing elit, sed do eiusmod tempor incididunt ut labore et dolore magna aliqua. Ut enim ad minim veniam, quis nostrud exercitation ullamco laboris nisi ut aliquip ex ea commodo consequat. Duis aute irure dolor in reprehenderit in voluptate velit esse cillum dolore eu fugiat nulla pariatur. Excepteur sint occaecat cupidatat non proident, sunt in culpa qui officia deserunt mollit anim id est laborum.</p>
  <p class="letter-body" style="top:278px">Lorem ipsum dolor sit amet, consectetur adipiscing elit, sed do eiusmod tempor incididunt ut labore et dolore magna aliqua. Ut enim ad minim veniam, quis nostrud exercitation ullamco laboris nisi ut aliquip ex ea commodo consequat. Duis aute irure dolor in reprehenderit in voluptate velit esse cillum dolore</p>
  <p class="letter-body" style="top:334px">Lorem ipsum dolor sit amet, consectetur adipiscing elit, sed do eiusmod tempor incididunt ut labore et dolore magna aliqua. Ut enim ad minim veniam, quis nostrud exercitation ullamco laboris nisi ut aliquip ex ea commodo consequat. Duis aute irure dolor in reprehenderit in voluptate velit esse cillum dolore eu fugiat nulla pariatur. Excepteur sint occaecat cupidatat non proident, sunt in culpa qui officia deserunt mollit anim id est laborum.</p>

  <div class="signoff" style="left:31px;top:441px">Sincerely,</div>
  <div class="signoff" style="left:30px;top:460px;line-height:15px">[ your Name ]<br>[ Title ]</div>
  <div class="signoff" style="right:26px;top:441px">Your Faithfully</div>

  <div class="letterhead__rule" style="top:535px"></div>
  <div class="letter-contact" style="top:546px">
    <span>801.574.2281 <svg class="icon" viewBox="0 0 10 10"><path d="M2 0h2l1 3-1.5 1a6 6 0 0 0 2.5 2.5L7 5l3 1v2c0 1-1 2-2 2A8 8 0 0 1 0 2c0-1 1-2 2-2z"/></svg></span>
    <span><svg class="icon" viewBox="0 0 10 10"><path d="M2 0h2l1 3-1.5 1a6 6 0 0 0 2.5 2.5L7 5l3 1v2c0 1-1 2-2 2A8 8 0 0 1 0 2c0-1 1-2 2-2z"/></svg> 801.846.5037</span>
  </div>
  <div class="letter-contact" style="top:557px">
    <span>neil@dunmorestucco-example.com <svg class="icon" viewBox="0 0 10 8"><rect width="10" height="8"/><path d="M0 0l5 4 5-4" stroke="#fff" fill="none"/></svg></span>
    <span><svg class="icon" viewBox="0 0 10 8"><rect width="10" height="8"/><path d="M0 0l5 4 5-4" stroke="#fff" fill="none"/></svg> amarla@dunmorestucco-example.com</span>
  </div>
  <div class="letter-contact" style="top:569px;font-size:5px">86 N. Maple #415 Orem, Utah 84093</div>
  <svg class="letterhead__corner-bottom" width="40" height="46" viewBox="0 0 40 46"><polygon points="40,0 40,46 0,46" fill="var(--black)"/></svg>
</section>

<!-- business card -->
<section class="sheet card">
  <div class="brand" style="left:141px;top:26px;gap:6px">
    <div class="brand__square" style="width:40px;height:60px"></div>
    <div class="brand__name" style="font-size:25px">Dunmore<br>Stucco</div>
  </div>
  <div class="card__rule"></div>
  <div class="card__emails">
    <div>marla@dunmorestucco-example.com <svg class="icon" viewBox="0 0 10 8"><rect width="10" height="8"/><path d="M0 0l5 4 5-4" stroke="#fff" fill="none"/></svg></div>
    <div>neil@dunmorestucco-example.com <svg class="icon" viewBox="0 0 10 8"><rect width="10" height="8"/><path d="M0 0l5 4 5-4" stroke="#fff" fill="none"/></svg></div>
  </div>
  <div class="card__phones">
    <div><b>Office</b>&nbsp;- 801.574.2281</div>
    <div><b>Mobile</b>&nbsp;- 801.846.5037</div>
  </div>
</section>

<!-- envelope -->
<section class="sheet envelope">
  <svg class="envelope__flap" width="463" height="51" viewBox="0 0 463 51"><polygon points="0,0 463,0 449,51 14,51" fill="var(--red)"/></svg>
  <div class="brand" style="left:181px;top:120px;gap:4px">
    <div class="brand__square" style="width:24px;height:35px"></div>
    <div class="brand__name" style="font-size:15px">Dunmore<br>Stucco</div>
  </div>
</section>

</body>
</html>
```